Solar accessories banner to produce more green energy

Hello,
we need a banner for a solar accessories page.
https://plovinta.de/index.php/zubehoer/
as we are commissioning the first banner for the entire homepage here, we are open to all directions. The current existing banner is just a random image of the installed theme and should not be a reference.
The banner should be created in a dark style. Our core colors are black / yellow / white.
The banner should have a clear reference to the accessories shown below and consider other accessories such as mounting systems of solar panels, cables, adapters, etc.
I would be happy to answer any queries.
Regards
Malte
-------------------------------------------------- ----------------------------------------------
Hello,
https://plovinta.de/index. php / accessories /
Since we are commissioning the first banner for the entire homepage, we are open to all directions. The currently existing banner is only a random image of the installed theme and is not intended to be a reference.
The banner should be created in a dark stem. Our core colors are black / yellow / white.
The banner should have a clear reference to the accessories shown below and take into account other accessories such as mounting systems for solar panels, cables, adapters, etc.
I am happy to answer any questions.
greetings
Malte

```html
<!DOCTYPE html>
<html lang="en">
<head>
<meta charset="utf-8">
<title>Mounting and connection accessories</title>
<link rel="stylesheet" href="https://fonts.googleapis.com/css2?family=Roboto:wght@300&display=swap">
<style>
  :root {
    --page-bg: #b9b9b9;
    --banner-bg: #140c02;
    --headline: #f5d90a;
    --body-text: #e6e2dc;
    --glow-yellow: #ffe81a;
    --glow-orange: #ff8a00;
    --glow-red: #e24a00;
  }
  html, body {
    margin: 0;
    width: 1200px;
    height: 1200px;
    overflow: hidden;
    background: var(--page-bg);
  }
  .banner {
    position: absolute;
    left: 50px;
    top: 410px;
    width: 1100px;
    height: 380px;
    background: var(--banner-bg);
    overflow: hidden;
    font-family: "Roboto", Arial, sans-serif;
    font-weight: 300;
  }
  .banner__visual {
    position: absolute;
    left: 600px;
    top: 0;
    width: 500px;
    height: 380px;
    background:
      radial-gradient(ellipse 70% 30% at 78% 62%, var(--glow-yellow) 0%, rgba(255,200,0,0.85) 35%, rgba(255,138,0,0) 100%),
      radial-gradient(ellipse 85% 45% at 70% 78%, var(--glow-orange) 0%, rgba(226,74,0,0.7) 45%, rgba(20,12,2,0) 100%),
      radial-gradient(ellipse 60% 20% at 60% 35%, rgba(255,138,0,0.55) 0%, rgba(20,12,2,0) 100%),
      linear-gradient(90deg, var(--banner-bg) 0%, rgba(20,12,2,0) 30%);
  }
  .banner__title {
    position: absolute;
    left: 60px;
    top: 92px;
    margin: 0;
    width: 560px;
    font-size: 50px;
    line-height: 54px;
    font-weight: 300;
    color: var(--headline);
    letter-spacing: 0.2px;
  }
  .banner__text {
    position: absolute;
    left: 57px;
    top: 222px;
    margin: 0;
    width: 560px;
    font-size: 17px;
    line-height: 21.5px;
    color: var(--body-text);
  }
</style>
</head>
<body>
  <section class="banner">
    <div class="banner__visual" role="img" aria-label="Glowing yellow and orange light trails flowing like cables across a dark background"></div>
    <h1 class="banner__title">Mounting and connection accessories</h1>
    <p class="banner__text">Our range of accessories is perfectly tailored to the products on offer.<br>You will find suitable plugs, cables, adapters, brackets and much<br>more for all areas.</p>
  </section>
</body>
</html>
```